Business Card Design

i am looking a business card for a car rental company long with Taxi service also a logo.

what is the latest with my project

Industry/Entity Type

Business

Contact Information for Business Card

name of the Company is Kestrel Bay Motor Leasing and Taxi Services
Address: Wren Hill Village, St. Corin's Parish Antigua
Tele# 555-0142/5550187-555-0163
Email: lorimbeck@quillmarsh.test

Font styles to use
Script

```html
<!DOCTYPE html>
<html lang="en">
<head>
<meta charset="utf-8">
<title>Kestrel Bay Motor Leasing and Taxi Services – Business Card</title>
<link rel="stylesheet" href="https://fonts.googleapis.com/css2?family=Kalam:wght@400&family=PT+Sans:wght@400&display=swap">
<style>
  :root {
    --backdrop: #e9e6e3;
    --card-white: #ffffff;
    --band-black: #000000;
    --accent-red: #e8202a;
    --brand-blue: #24479b;
    --strip-grey: #a9a9a9;
    --taxi-yellow: #f5c515;
    --taxi-amber: #e09a0a;
    --text-white: #ffffff;
  }
  html, body {
    margin: 0;
    width: 1200px;
    height: 800px;
    overflow: hidden;
    background: var(--backdrop);
  }
  .business-card {
    position: absolute;
    left: 100px;
    top: 114px;
    width: 1000px;
    height: 572px;
    background: var(--card-white);
    overflow: hidden;
    box-shadow: 0 6px 24px rgba(0,0,0,0.18);
  }
  .taxi-illustration {
    position: absolute;
    left: 60px;
    top: 18px;
    width: 270px;
    height: 236px;
    border-radius: 40px 40px 22px 22px;
    background: radial-gradient(ellipse at 45% 40%, var(--taxi-yellow) 0%, var(--taxi-amber) 70%, #8a8a8a 100%);
  }
  .brand-lockup {
    position: absolute;
    right: 60px;
    top: 70px;
    display: flex;
    align-items: center;
    gap: 22px;
  }
  .brand-mark {
    width: 86px;
    height: 86px;
    border-radius: 50%;
    background: var(--brand-blue);
    flex: none;
  }
  .brand-name {
    font-family: "Kalam", cursive;
    font-weight: 400;
    font-size: 34px;
    line-height: 1.15;
    color: var(--accent-red);
    margin: 0;
    text-align: center;
  }
  .checker-strip {
    position: absolute;
    left: 0;
    top: 262px;
    width: 100%;
    height: 14px;
    background: var(--strip-grey);
  }
  .contact-band {
    position: absolute;
    left: 0;
    top: 276px;
    width: 100%;
    height: 252px;
    background: var(--band-black);
  }
  .contact-list {
    list-style: none;
    margin: 0;
    padding: 34px 0 0 70px;
    font-family: "PT Sans", sans-serif;
    font-size: 31px;
    line-height: 46px;
    color: var(--text-white);
    letter-spacing: 0.3px;
  }
  .accent-stripe {
    position: absolute;
    left: 0;
    top: 528px;
    width: 100%;
    height: 16px;
    background: var(--accent-red);
  }
  .base-edge {
    position: absolute;
    left: 0;
    top: 544px;
    width: 100%;
    height: 28px;
    background: var(--band-black);
  }
</style>
</head>
<body>
  <article class="business-card">
    <div class="taxi-illustration" role="img" aria-label="Illustration of a yellow taxi cab with a checkered roof sign"></div>

    <div class="brand-lockup">
      <span class="brand-mark" aria-hidden="true"></span>
      <h1 class="brand-name">Kestrel Bay Motor Leasing<br>and Taxi Services</h1>
    </div>

    <div class="checker-strip" role="img" aria-label="Checkered taxi strip"></div>

    <section class="contact-band">
      <ul class="contact-list">
        <li class="contact-address">Wren Hill Village, St. Corin's Parish Antigua</li>
        <li class="contact-phone">Tele: 555-0142/5550187-555-0163</li>
        <li class="contact-email">Email: lorimbeck@quillmarsh.test</li>
      </ul>
    </section>

    <div class="accent-stripe"></div>
    <div class="base-edge"></div>
  </article>
</body>
</html>
```